Letter and Services

Our current letter is two sided, one tells about our company, and the other lists our services in the same categories as found on our website. We like light and bright marketing and are looking from a change over our old materials. Whites, the teal in our logo, greys, etc. modern, clean, upscale feeling. We can provide updated text for the letter to go with the marketing materials.

```html
<!DOCTYPE html>
<html lang="en">
<head>
<meta charset="utf-8">
<title>Juniper Row Properties – Letter and Services</title>
<link rel="stylesheet" href="https://fonts.googleapis.com/css2?family=Montserrat:ital,wght@0,400;0,500;0,600;0,700;1,700&display=swap">
<style>
  :root {
    --teal: #137f83;
    --teal-dark: #0f6e72;
    --ink: #2b2b2b;
    --grey-line: #b9b9b9;
    --backdrop: #8e8e8e;
    --paper: #ffffff;
    --paper-shade: #eeeff0;
  }
  * { margin: 0; padding: 0; box-sizing: border-box; }
  html, body { width: 1200px; height: 839px; overflow: hidden; }
  body {
    background: var(--backdrop);
    font-family: "Montserrat", sans-serif;
    color: var(--ink);
    position: relative;
  }
  .page {
    position: absolute;
    top: 79px;
    width: 469px;
    height: 663px;
    background: var(--paper);
    overflow: hidden;
  }
  .page--letter { left: 109px; }
  .page--services {
    left: 620px;
    background: linear-gradient(180deg, #e9eaeb 0%, #ffffff 25%, #f6f6f7 75%, var(--paper-shade) 100%);
  }

  /* Letter */
  .brand-name {
    position: absolute;
    right: 38px;
    top: 62px;
    display: flex;
    align-items: center;
    gap: 7px;
    font-size: 15px;
    font-weight: 600;
    color: var(--ink);
    letter-spacing: 0.2px;
  }
  .brand-name__mark {
    width: 11px; height: 11px;
    background: var(--teal);
  }
  .tree-art {
    position: absolute;
    left: 277px; top: 388px;
    width: 192px; height: 236px;
    background: radial-gradient(ellipse at 60% 40%, rgba(200,202,204,0.55) 0%, rgba(220,222,224,0.35) 45%, rgba(255,255,255,0) 75%);
  }
  .letter__greeting {
    position: absolute;
    left: 47px; top: 152px;
    font-size: 14.5px;
    font-weight: 700;
    font-style: italic;
    color: var(--teal-dark);
  }
  .letter__body {
    position: absolute;
    left: 47px; top: 178px;
    width: 332px;
    font-size: 9.3px;
    line-height: 12px;
  }
  .letter__body p + p { margin-top: 9.6px; }
  .signature {
    position: absolute;
    left: 47px; top: 510px;
  }
  .signature__rule {
    width: 112px; height: 1px; background: var(--grey-line);
    margin-bottom: 9px;
  }
  .signature p { font-size: 11px; line-height: 13px; }
  .signature .signature__name { color: var(--teal); }

  /* Footer */
  .page-footer__rule {
    position: absolute;
    height: 1px; background: var(--grey-line);
  }
  .page-footer__accent {
    position: absolute;
    height: 4px; background: var(--teal);
    border-radius: 2px;
  }
  .contact-row {
    position: absolute;
    display: flex;
    align-items: center;
    gap: 9px;
    font-size: 8.6px;
    font-weight: 600;
    color: var(--ink);
    white-space: nowrap;
  }
  .contact-item { display: flex; align-items: center; gap: 5px; }
  .contact-item svg { width: 10px; height: 10px; flex: none; }

  /* Services */
  .photo-band {
    position: absolute;
    left: 0; top: 32px;
    width: 469px; height: 85px;
    background: var(--teal);
  }
  .photo {
    position: absolute;
    top: 6px; height: 73px;
  }
  .photo--house { left: 0; width: 111px; background: linear-gradient(180deg, #8fb0d0 0%, #c8c3b8 45%, #5f8a3c 100%); }
  .photo--living { left: 117px; width: 112px; background: linear-gradient(180deg, #d8d2c8 0%, #3e6a68 45%, #7a4a2c 100%); }
  .photo--nook { left: 234px; width: 115px; background: linear-gradient(180deg, #b7c9a6 0%, #e8e8e6 50%, #8c8c88 100%); }
  .photo--couple { left: 354px; width: 115px; background: linear-gradient(135deg, #e9e4dc 0%, #d6b49a 50%, #8fb2c8 100%); }

  .services-frame {
    position: absolute;
    left: 22px; top: 150px;
    width: 424px; height: 441px;
    border: 1.2px solid var(--teal);
    border-radius: 12px;
  }
  .services-title {
    position: absolute;
    left: 0; right: 0; top: 140px;
    text-align: center;
  }
  .services-title span {
    display: inline-block;
    padding: 0 14px;
    background: #fafafa;
    font-size: 15.5px;
    font-weight: 700;
    letter-spacing: 0.3px;
    color: var(--ink);
  }
  .service {
    position: absolute;
    width: 186px;
  }
  .service__heading {
    height: 13px;
    border-radius: 7px;
    background: linear-gradient(90deg, var(--teal-dark), #1a9599);
    color: #fff;
    font-size: 8.6px;
    font-weight: 600;
    letter-spacing: 0.3px;
    text-align: center;
    line-height: 13px;
    margin-bottom: 5px;
  }
  .service ul {
    list-style: none;
    padding-left: 8px;
  }
  .service li {
    position: relative;
    font-size: 7.6px;
    line-height: 9.6px;
    margin-bottom: 4.2px;
  }
  .service li::before {
    content: "";
    position: absolute;
    left: -7px; top: 3.6px;
    width: 2.2px; height: 2.2px;
    border-radius: 50%;
    background: var(--teal);
  }
</style>
</head>
<body>

<section class="page page--letter">
  <div class="brand-name"><span class="brand-name__mark"></span>Juniper Row Properties</div>

  <div class="tree-art" role="img" aria-label="Faint decorative tree with perched birds"></div>

  <h1 class="letter__greeting">HELLO!</h1>
  <div class="letter__body">
    <p>We love real estate. We buy it, sell it, renovate it, restore it, and rent it. We value the unique qualities that properties possess. We also value friendly customer service and good old fashioned common sense. It's easy for us, since we love what we do.</p>
    <p>We believe that honesty and integrity are fundamental, and we pledge to treat our clients well.</p>
    <p>We believe that everyone deserves a well maintained home. We commit to caring for all rental properties as we would treat our own home, and to meet our tenants and clients needs as quickly as possible. We know that keeping clients happy means servicing them well. We utilize the newest technology to make life easy.</p>
    <p>With over 15 years in property management, and 20 years in real estate, our team knows their stuff. We are well versed in Fair Housing laws, mold remediation, preventative maintenance programs, landlord-tenant law, general property repair, and much more. If we don't have an answer to your question, we have long standing relationships with legal and financial professionals and we'll get the info you need.</p>
    <p>Our team members hold both the Certified Residential Manager (CRM) and Certified Commercial Manager (CCM) designations from the Council of Property Managers. With experience in single family, multifamily, and commercial property managment, we are dedicated to meeting the highest standards of our industry. Ordinary is just not our style.</p>
  </div>

  <div class="signature">
    <div class="signature__rule"></div>
    <p>Sincerely</p>
    <p class="signature__name">Claire and Dana</p>
    <p class="signature__name">Juniper Row Properties</p>
  </div>

  <div class="page-footer__rule" style="left:27px; top:616px; width:416px;"></div>
  <div class="page-footer__accent" style="left:173px; top:614px; width:122px;"></div>
  <div class="contact-row" style="left:23px; top:632px;">
    <span class="contact-item">
      <svg viewBox="0 0 10 10"><circle cx="5" cy="5" r="5" fill="var(--teal)"/><path d="M3.2 2.6c.3-.2.6-.2.8.1l.5.8c.1.2 0 .4-.1.6l-.3.3c.3.6.8 1.1 1.4 1.4l.3-.3c.2-.1.4-.2.6-.1l.8.5c.3.2.3.5.1.8-.4.5-1 .7-1.6.4C4.6 6.4 3.6 5.4 3 4.3c-.3-.6-.2-1.2.2-1.7z" fill="#fff"/></svg>
      555.014.2290
    </span>
    <span class="contact-item">
      <svg viewBox="0 0 10 10"><circle cx="5" cy="5" r="5" fill="var(--teal)"/><circle cx="5" cy="5" r="2.8" fill="none" stroke="#fff" stroke-width=".6"/><path d="M2.2 5h5.6M5 2.2c-1.3 1.6-1.3 4 0 5.6M5 2.2c1.3 1.6 1.3 4 0 5.6" fill="none" stroke="#fff" stroke-width=".5"/></svg>
      hello@juniperrowproperties.com
    </span>
    <span class="contact-item">
      <svg viewBox="0 0 10 10"><circle cx="5" cy="5" r="5" fill="var(--teal)"/><rect x="2.6" y="3.3" width="4.8" height="3.4" rx=".4" fill="#fff"/><path d="M2.8 3.5 5 5.2l2.2-1.7" fill="none" stroke="var(--teal)" stroke-width=".5"/></svg>
      www.juniperrowproperties.com
    </span>
  </div>
</section>

<section class="page page--services">
  <div class="photo-band">
    <div class="photo photo--house" role="img" aria-label="Photo of a two-storey suburban house with a green lawn"></div>
    <div class="photo photo--living" role="img" aria-label="Photo of a living room with hardwood floors and a teal accent wall"></div>
    <div class="photo photo--nook" role="img" aria-label="Photo of a bright window nook with white chairs"></div>
    <div class="photo photo--couple" role="img" aria-label="Photo of a smiling couple"></div>
  </div>

  <div class="services-frame"></div>
  <h2 class="services-title"><span>OUR SERVICES</span></h2>

  <div class="service" style="left:36px; top:180px;">
    <h3 class="service__heading">INVESTMENT PROPERTY SELECTION</h3>
    <ul>
      <li>Analyze current or prospective investment properties to determine prospective return on investment.</li>
      <li>Recommend rental rates and/or improvements to increase profitability.</li>
      <li>Assist in the search and purchase of properties to grow your portfolio.</li>
    </ul>
  </div>

  <div class="service" style="left:246px; top:180px;">
    <h3 class="service__heading">TENANT PROCUREMENT</h3>
    <ul>
      <li>A broad scope of advertising initiatives to lease your property quickly.</li>
      <li>Tenant screening with comprehensive background check, employment verification, landlord verification, and reference check.</li>
      <li>In person as well as online applications and lease signing available to secure a lease for your property quickly.</li>
    </ul>
  </div>

  <div class="service" style="left:36px; top:302px;">
    <h3 class="service__heading">LEASE ADMINISTRATION</h3>
    <ul>
      <li>Tenant move-in information packet and gift.</li>
      <li>Move-in inspection and quarterly property inspections.</li>
      <li>Monthly check-in with Tenant. Rent collection with online payment and automatic debit options for tenants.</li>
      <li>Payment of property invoices.</li>
      <li>Active resident retention and lease renewals.</li>
      <li>Addressing lease violations and working with our attorney or yours for legal action when necessary.</li>
    </ul>
  </div>

  <div class="service" style="left:246px; top:302px;">
    <h3 class="service__heading">REPAIRS AND MAINTENANCE</h3>
    <ul>
      <li>Creation and implementation of a preventative maintenance plan.</li>
      <li>Coordination of standard repairs and tenant work orders.</li>
      <li>Creation of capital improvement plan and implementation as per client’s direction.</li>
      <li>Vendor negotiations.</li>
      <li>Contract execution and enforcement.</li>
      <li>24/7 Emergency maintenance with on call service.</li>
    </ul>
  </div>

  <div class="service" style="left:36px; top:465px;">
    <h3 class="service__heading">MOVE OUT &amp; TURNOVER</h3>
    <ul>
      <li>Move out property inspection with tenant.</li>
      <li>Security Deposit charges, refunds, and accounting, in accordance with PA state law.</li>
      <li>If applicable, aggressive collection of any charges above security deposit.</li>
      <li>Arrangement and management of vendors to prepare the property for the new tenant.</li>
    </ul>
  </div>

  <div class="service" style="left:246px; top:465px;">
    <h3 class="service__heading">ADDITIONAL OWNER BENEFITS</h3>
    <ul>
      <li>Customized owner portal with easy access to real time reports, work orders and notes, and tenant communication.</li>
      <li>Monthly property overview report emailed and mailed.</li>
      <li>Annual property report with recommended revenue increases, five year capital plan with suggested improvements, and end of the year tax forms.</li>
    </ul>
  </div>

  <div class="page-footer__rule" style="left:26px; top:617px; width:417px;"></div>
  <div class="page-footer__accent" style="left:173px; top:615px; width:122px;"></div>
  <div class="contact-row" style="left:22px; top:634px;">
    <span class="contact-item">
      <svg viewBox="0 0 10 10"><circle cx="5" cy="5" r="5" fill="var(--teal)"/><path d="M3.2 2.6c.3-.2.6-.2.8.1l.5.8c.1.2 0 .4-.1.6l-.3.3c.3.6.8 1.1 1.4 1.4l.3-.3c.2-.1.4-.2.6-.1l.8.5c.3.2.3.5.1.8-.4.5-1 .7-1.6.4C4.6 6.4 3.6 5.4 3 4.3c-.3-.6-.2-1.2.2-1.7z" fill="#fff"/></svg>
      555.014.2290
    </span>
    <span class="contact-item">
      <svg viewBox="0 0 10 10"><circle cx="5" cy="5" r="5" fill="var(--teal)"/><circle cx="5" cy="5" r="2.8" fill="none" stroke="#fff" stroke-width=".6"/><path d="M2.2 5h5.6M5 2.2c-1.3 1.6-1.3 4 0 5.6M5 2.2c1.3 1.6 1.3 4 0 5.6" fill="none" stroke="#fff" stroke-width=".5"/></svg>
      hello@juniperrowproperties.com
    </span>
    <span class="contact-item">
      <svg viewBox="0 0 10 10"><circle cx="5" cy="5" r="5" fill="var(--teal)"/><rect x="2.6" y="3.3" width="4.8" height="3.4" rx=".4" fill="#fff"/><path d="M2.8 3.5 5 5.2l2.2-1.7" fill="none" stroke="var(--teal)" stroke-width=".5"/></svg>
      www.juniperrowproperties.com
    </span>
  </div>
</section>

</body>
</html>
```